Dog care service needs advertising poster

Our company is Paw Haven. We provide care for dogs while their owners are away, either through home visits or a holiday stay in the homes of carefully selected minders. Our existing website & Facebook cover should provide all the colour cues for a poster - namely blues, blondes and grey. We have an existing logo (provided). We can feature the same imagery from our website as I have purchased the rights to the stock images.

www.pawhavenexample.com.au
www.facebook.com/pawhavenexampleau

This brief is for design of a poster that can be placed in vet surgeries, groomers, on community noticeboards. It should be scalable to print in three sizes, A5, A4 & A3.

We wish to clearly communicate our three areas of service "dog minding, home visits, dog walking".

We would like to have the files ready for upload to Printora (or similar) for immediate printing.

Target Market(s)

Dog owners who love their dogs like family.

Industry/Entity Type

Advertising

Font styles to use
Sans Serif

Colors
33a6d7
3276b5

Requirements
Must have
• Logo
• www.pawhavenexample.com.au
• Telephone number
• Three services - Dog Minding, Home Visits, Dog Walking
Nice to have
• use of our existing stock photography to highlight the three areas of service - Dog minding, home visits, dog walking. Existing colour palette - blues, blondes and grey.
• Text that can be used:
• Western Sydney’s complete dog care service.
• Dog Minding - Your dog stays in the home of one of our carefully selected minders.Treated like part of the family, they enjoy all the creature comforts they are used to.
• Home Visits - We visit your dog at your home for feeding, walking and playtime. Short of long visits available.
• Dog Walking - If you can't walk your dog for any reason we are here to help. 1/2 hour or hourly walks available.
• Contact us today for a tailored package to meet your needs.
Should not have
• Any additional illustrations beyond the logo.

```html
<!DOCTYPE html>
<html lang="en">
<head>
<meta charset="utf-8">
<title>Paw Haven – Dog Care Poster</title>
<link href="https://fonts.googleapis.com/css2?family=Lato:wght@400;700;900&display=swap" rel="stylesheet">
<style>
  :root {
    --sky: #33a6d7;
    --blue: #3276b5;
    --slate: #3d4a5c;
    --slate-dark: #2f3947;
    --grey: #6f7275;
    --grey-light: #c9cccf;
    --band: #7a7873;
    --white: #ffffff;
    --page: #e6e7e9;
    --ink: #2a3340;
  }
  * { box-sizing: border-box; margin: 0; padding: 0; }
  html, body { width: 1200px; height: 1023px; overflow: hidden; }
  body {
    background: var(--page);
    font-family: "Lato", Arial, sans-serif;
    display: flex; align-items: center; justify-content: center;
  }
  .poster {
    position: relative;
    width: 700px; height: 990px;
    background: var(--white);
    overflow: hidden;
    box-shadow: 0 4px 18px rgba(0,0,0,.18);
  }

  /* Header */
  .hero-photo {
    position: absolute; left: 0; top: 0; width: 700px; height: 300px;
    background: linear-gradient(100deg, #dfe6ea 0%, #b9c6ce 40%, #7f95a3 70%, #c79a55 88%, #8a6a3e 100%);
  }
  .brand {
    position: absolute; left: 34px; top: 30px;
    display: flex; align-items: center; gap: 14px;
  }
  .brand-mark { width: 46px; height: 46px; border-radius: 50%; background: var(--slate); }
  .brand-name { font-size: 36px; font-weight: 700; color: var(--slate); line-height: 1; }
  .brand-sub { font-size: 12px; font-weight: 700; color: var(--slate); letter-spacing: 4px; margin-top: 5px; }
  .tagline {
    position: absolute; left: 0; top: 150px; width: 440px; height: 72px;
    background: var(--band);
    clip-path: polygon(0 0, 100% 0, 92% 100%, 0 100%);
    padding: 10px 0 0 40px; color: var(--white);
  }
  .tagline strong { display: block; font-size: 25px; font-weight: 900; letter-spacing: .5px; }
  .tagline span { font-size: 19px; }
  .services-label {
    position: absolute; right: 44px; top: 256px;
    font-size: 30px; letter-spacing: 8px; color: var(--white); font-weight: 400;
  }

  /* Service rows */
  .service {
    position: absolute; left: 0; width: 700px; height: 172px;
    display: flex;
  }
  .service-text {
    width: 300px; height: 100%;
    padding: 24px 26px 0 34px;
    color: var(--white); font-size: 17px; line-height: 1.35;
    clip-path: polygon(0 0, 100% 0, 100% 38%, 92% 50%, 100% 62%, 100% 100%, 0 100%);
  }
  .service-photo { width: 320px; height: 100%; border-top: 4px solid var(--white); }
  .service-name {
    width: 80px; height: 100%;
    display: flex; align-items: center; justify-content: center;
    color: var(--white); font-size: 24px; font-weight: 400; letter-spacing: 1px;
    writing-mode: vertical-rl;
  }
  .minding { top: 300px; }
  .minding .service-text { background: var(--sky); }
  .minding .service-photo { background: linear-gradient(180deg, #cfe8f2 0%, #9bc58a 55%, #5f9a3c 100%); }
  .minding .service-name { background: var(--sky); }

  .visits { top: 472px; }
  .visits .service-text { background: var(--blue); }
  .visits .service-photo { background: linear-gradient(180deg, #f1f1ee 0%, #d9d2c4 50%, #a58a62 100%); }
  .visits .service-name { background: var(--blue); }

  .walking { top: 644px; }
  .walking .service-text { background: var(--slate); }
  .walking .service-photo { background: linear-gradient(180deg, #a7c08c 0%, #6f9a4c 55%, #4f8a34 100%); }
  .walking .service-name { background: var(--slate); }

  /* Footer */
  .contact {
    position: absolute; left: 0; top: 816px; width: 300px; height: 94px;
    background: var(--slate-dark);
    padding: 20px 0 0 34px; color: var(--white);
  }
  .contact .web { font-size: 16px; letter-spacing: .5px; }
  .contact .phone { font-size: 22px; letter-spacing: 2px; margin-top: 6px; }
  .footer-grey {
    position: absolute; left: 300px; top: 816px; width: 400px; height: 94px;
    background: var(--grey-light);
  }
  .cta {
    position: absolute; left: 0; top: 910px; width: 700px; height: 80px;
    background: var(--grey);
    color: var(--white); font-size: 22px; font-weight: 700; letter-spacing: 1px;
    display: flex; align-items: center; justify-content: center; text-align: center;
  }
</style>
</head>
<body>
  <main class="poster">
    <div class="hero-photo" role="img" aria-label="Golden retriever looking out of a car window"></div>
    <div class="brand">
      <span class="brand-mark"></span>
      <div>
        <div class="brand-name">Paw Haven</div>
        <div class="brand-sub">PET SERVICES</div>
      </div>
    </div>
    <div class="tagline">
      <strong>Western Sydney’s</strong>
      <span>complete dog care service</span>
    </div>
    <div class="services-label">SERVICES</div>

    <section class="service minding">
      <p class="service-text">Your dog stays in the home of one of our carefully selected minders. Treated like part of the family, they enjoy all the creature comforts they are used to.</p>
      <div class="service-photo" role="img" aria-label="Happy dog running on green grass"></div>
      <h2 class="service-name">Dog Minding</h2>
    </section>

    <section class="service visits">
      <p class="service-text">We visit your dog at your home for feeding, walking and playtime. Short or long visits available.</p>
      <div class="service-photo" role="img" aria-label="Small dog lying on a home doormat"></div>
      <h2 class="service-name">Home Visits</h2>
    </section>

    <section class="service walking">
      <p class="service-text">If you can’t walk your dog for any reason we are here to help. 1/2 hour or hourly walks available.</p>
      <div class="service-photo" role="img" aria-label="Bulldog on a lead walking across a park lawn"></div>
      <h2 class="service-name">Dog Walking</h2>
    </section>

    <div class="contact">
      <div class="web">www.pawhavenexample.com.au</div>
      <div class="phone">Phone: 0491 570 156</div>
    </div>
    <div class="footer-grey"></div>
    <div class="cta">Contact us today for a tailored package to meet your needs</div>
  </main>
</body>
</html>
```